Single brochure for international companies in the financial sector

We need to update a brochure 4 pages presenting our company. We are a financial engineering company. The final design must provide financial security, service and trust. you will find the current brochure copy. Our color code is Orange (RGB 235/100/68), Black, White and Gray. photos show the visual of the site, but it is not mandatory to keep them.

Target Market(s)

wealth management professionals

Industry/Entity Type

Finance

Requirements
Must have
• Logo Tolvane Capital all text in the document color Orange Tolvane (RGB 235/100/68)
Nice to have
• Vista Font
Should not have
• images / pictures of people

```html
<!DOCTYPE html>
<html lang="en">
<head>
<meta charset="utf-8">
<title>Tolvane Capital – Brochure Spreads</title>
<link href="https://fonts.googleapis.com/css2?family=Jost:wght@300;400;500;600&display=swap" rel="stylesheet">
<style>
  :root {
    --orange: rgb(235, 100, 68);
    --orange-soft: rgba(235, 100, 68, 0.22);
    --black: #111111;
    --ink: #222222;
    --white: #ffffff;
    --stage-top: #c9c9c9;
    --stage-mid: #eeeeee;
  }
  * { box-sizing: border-box; margin: 0; padding: 0; }
  html, body { width: 1200px; height: 1200px; overflow: hidden; }
  body {
    background: radial-gradient(ellipse at 50% 55%, var(--stage-mid) 0%, #dedede 55%, var(--stage-top) 100%);
    font-family: "Jost", "Helvetica Neue", Arial, sans-serif;
    color: var(--ink);
    position: relative;
  }
  .page {
    position: absolute;
    top: 405px;
    width: 275px;
    height: 390px;
    background: var(--white);
    overflow: hidden;
    box-shadow: 0 2px 6px rgba(0,0,0,0.12);
  }
  .page--cover { left: 32px; }
  .page--company { left: 326px; }
  .page--services { left: 619px; }
  .page--back { left: 909px; background: var(--orange); }

  /* plain name mark: one colour, one weight, small square beside it */
  .name-mark {
    display: inline-flex; align-items: center; gap: 6px;
    font-weight: 400; letter-spacing: 0; white-space: nowrap;
  }
  .name-mark__square { display: inline-block; background: currentColor; }

  /* cover */
  .cover-brand {
    position: absolute; top: 140px; left: 0; width: 100%;
    text-align: center; color: var(--black);
  }
  .cover-brand .name-mark { font-size: 20px; gap: 8px; }
  .cover-brand .name-mark__square { width: 9px; height: 9px; }
  .cover-band {
    position: absolute; left: 0; top: 258px; width: 100%; height: 132px;
  }
  .band-rule {
    position: absolute; left: 0; width: 100%; height: 6px;
    background: linear-gradient(to bottom, #f5f5f5, #9a9a9a);
  }
  .band-rule::after {
    content: ""; position: absolute; left: 0; bottom: -1px; width: 100%; height: 2px;
    background: linear-gradient(to right, #d0d0d0, var(--black) 60%, var(--black));
  }
  .band-fill { position: absolute; left: 0; width: 100%; background: var(--orange); }
  .cover-band .band-fill { top: 8px; bottom: 0; }
  .cover-tagline {
    position: absolute; right: 34px; top: 60px;
    color: var(--white); font-weight: 300; font-size: 17px; line-height: 16px;
    text-align: right; letter-spacing: -0.3px;
    padding-right: 8px; border-right: 1px solid var(--white);
  }

  /* inner pages */
  .section-title {
    position: absolute; left: 22px; top: 42px;
    border-left: 2px solid var(--orange); padding-left: 11px; height: 28px;
    font-size: 21px; font-weight: 400; letter-spacing: -1.2px; line-height: 28px;
  }
  .section-title__lead { color: var(--black); }
  .section-title__accent { color: var(--orange); }
  .section-title__echo {
    position: absolute; left: 26px; top: -5px; white-space: nowrap;
    color: var(--orange-soft); font-weight: 300; letter-spacing: -1px;
  }
  .statement {
    position: absolute; text-align: right; white-space: nowrap;
    font-size: 12px; line-height: 13px; font-weight: 500;
    color: var(--black); letter-spacing: -0.4px; text-transform: uppercase;
  }
  .statement .accent { color: var(--orange); }
  .statement p + p { margin-top: 10px; }
  .page--services .statement { line-height: 14.6px; font-size: 12.5px; }
  .copy-column { position: absolute; width: 102px; }
  .copy-block + .copy-block { margin-top: 9px; }
  .copy-block__title {
    font-size: 9px; font-weight: 500; color: var(--black);
    text-transform: uppercase; letter-spacing: -0.2px; margin-bottom: 2px;
  }
  .copy-block__text {
    font-size: 5.4px; line-height: 7px; color: var(--ink); text-align: justify;
  }
  .page-footer { position: absolute; left: 0; top: 352px; width: 100%; height: 38px; }
  .page-footer .band-fill { top: 7px; bottom: 0; }
  .footer-brand {
    position: absolute; left: 20px; top: 19px; color: var(--white);
  }
  .footer-brand .name-mark { font-size: 6px; gap: 3px; }
  .footer-brand .name-mark__square { width: 3px; height: 3px; }

  .page--company .statement { right: 151px; top: 157px; }
  .page--company .copy-column { left: 139px; top: 134px; }
  .page--services .statement { right: 155px; top: 148px; }
  .page--services .copy-column { left: 134px; top: 108px; }
  .page--services .copy-block + .copy-block { margin-top: 14px; }

  /* back */
  .back-art {
    position: absolute; left: 0; top: 205px; width: 100%; height: 160px;
    background: linear-gradient(170deg, rgba(255,255,255,0) 30%, rgba(255,255,255,0.07) 60%, rgba(0,0,0,0.04));
  }
  .back-brand {
    position: absolute; left: 0; top: 288px; width: 100%; text-align: center;
    color: var(--white);
  }
  .back-brand .name-mark { font-size: 9px; gap: 4px; }
  .back-brand .name-mark__square { width: 4px; height: 4px; }
  .back-details {
    position: absolute; left: 0; top: 318px; width: 100%; text-align: center;
    color: var(--white); font-size: 4.2px; line-height: 6.5px;
  }
  .back-details__web { font-size: 5px; font-weight: 600; margin-top: 6px; }
</style>
</head>
<body>

<section class="page page--cover" aria-label="Front cover">
  <div class="cover-brand">
    <span class="name-mark"><span class="name-mark__square"></span>Tolvane Capital</span>
  </div>
  <div class="cover-band">
    <div class="band-rule"></div>
    <div class="band-fill" role="img" aria-label="Orange band with a faint line drawing of a stone arch bridge"></div>
    <div class="cover-tagline">FINANCIAL<br>ENGINEERING</div>
  </div>
</section>

<section class="page page--company" aria-label="The company">
  <h2 class="section-title">
    <span class="section-title__echo">THE COMPANY</span>
    <span class="section-title__lead">THE</span><span class="section-title__accent">COMPANY</span>
  </h2>
  <div class="statement">
    <p><span class="accent">Our clients</span><br>must deliver<br>performance<br>on their<br>portfolios on a<br>regular basis</p>
    <p class="accent">We help them<br>deliver everyday</p>
  </div>
  <div class="copy-column">
    <div class="copy-block">
      <h3 class="copy-block__title">About us</h3>
      <p class="copy-block__text">Tolvane Capital is a financial engineering company.<br>It is fully independent from any bank or any other company.</p>
    </div>
    <div class="copy-block">
      <h3 class="copy-block__title">Our clients</h3>
      <p class="copy-block__text">Our clients are financial professionals such as asset managers, institutionnals, corporates, private banks, wealth managers and family offices.<br>Our purpose is to make their work easier, every day.</p>
    </div>
    <div class="copy-block">
      <h3 class="copy-block__title">What we do</h3>
      <p class="copy-block__text">We provide them with investment solutions designed to improve their portfolios performance.<br>Simple as that.</p>
    </div>
  </div>
  <div class="page-footer">
    <div class="band-rule"></div>
    <div class="band-fill"></div>
    <div class="footer-brand"><span class="name-mark"><span class="name-mark__square"></span>Tolvane Capital</span></div>
  </div>
</section>

<section class="page page--services" aria-label="Our services">
  <h2 class="section-title">
    <span class="section-title__echo">OUR SERVICES</span>
    <span class="section-title__lead">OUR</span><span class="section-title__accent">SERVICES</span>
  </h2>
  <div class="statement">
    <p><span class="accent">Tolvane<br>Capital's</span><br>core business<br>is the design<br>and selection<br>of investment<br>solutions</p>
  </div>
  <div class="copy-column">
    <div class="copy-block">
      <h3 class="copy-block__title">Investment advice</h3>
      <p class="copy-block__text">Each client is looking for a unique investment solution. Hence, we combine internal and external resources to create the financial product that will best fit our clients requirements. Thanks to a truly independent advice, we offer bespoke, simple and efficient solutions.</p>
    </div>
    <div class="copy-block">
      <h3 class="copy-block__title">Portfolio analysis</h3>
      <p class="copy-block__text">We advise our clients on their portfolios of financial products. Together we identify the needs for restructuring or reallocating the assets. We also provide full monitoring and reporting services throughout the life of the products.</p>
    </div>
    <div class="copy-block">
      <h3 class="copy-block__title">Partner selection</h3>
      <p class="copy-block__text">Our internal tools allow us to continuously assess the issuers we are working with.<br>Therefore we give our clients the luxury to chose among the best issuers for their investment solution.</p>
    </div>
  </div>
  <div class="page-footer">
    <div class="band-rule"></div>
    <div class="band-fill"></div>
    <div class="footer-brand"><span class="name-mark"><span class="name-mark__square"></span>Tolvane Capital</span></div>
  </div>
</section>

<section class="page page--back" aria-label="Back cover">
  <div class="back-art" role="img" aria-label="Faint tone-on-tone line drawing of an arch bridge"></div>
  <div class="back-brand">
    <span class="name-mark"><span class="name-mark__square"></span>Tolvane Capital</span>
  </div>
  <div class="back-details">
    <p>Tolvane Capital SA. Capital : 400 000 Euros</p>
    <p>RCS Lyon : 812 447 205</p>
    <p>Code Banque (CIB) : 10457</p>
    <p class="back-details__web">www.tolvanecapital.com</p>
  </div>
</section>

</body>
</html>
```